Flyer-Design für Immobilienmakler
Zielgruppe
Immobilienmakler. Zielgruppe: Hausverkäufer im mittleren und älteren Alter.
Aufgabenstellung
Textvorschlag:
Eine kostenlose Immobilienbewertung bekommen Sie von jedem Makler, wir reduzieren zusätzlich unsere Vermittlungsprovision.
Sparen Sie jetzt 2 %* Provision
Alles wird teurer. Wir reduzieren die Provision!
Wir helfen bei der Verwirklichung Ihres Wohntraums. Angebot gültig gegen Vorlage des Flyers.
*Bei uns 2 % weniger:
• Übliche Maklerprovision 5,95 %
• 3,95 % bedeutet Alleinprovision oder geteilte Provision 1,97 %
• Gilt ab ein Verkaufswert von 400.000,- Euro
• Gültig bis 30. Dezember 2022
• Nur gegen Vorlage des Flyers
und Alleinauftrag.

```html
<!DOCTYPE html>
<html lang="de">
<head>
<meta charset="utf-8">
<title>Flyer – Provision sparen</title>
<link rel="stylesheet" href="https://fonts.googleapis.com/css2?family=Roboto:wght@100;300;400;500;700&display=swap">
<style>
  :root {
    --green: #b0cb36;
    --green-deep: #a9c233;
    --white: #ffffff;
    --ink: #1f1f1f;
    --navy: #0d2a48;
    --leaf: #3e8a3b;
  }
  html, body {
    margin: 0;
    padding: 0;
    overflow: hidden;
    background: var(--white);
  }
  .flyer {
    position: relative;
    width: 845px;
    height: 1200px;
    overflow: hidden;
    background: var(--white);
    font-family: "Roboto", Arial, sans-serif;
  }
  .hero-band {
    position: absolute;
    left: 0;
    top: 0;
    width: 845px;
    height: 760px;
  }
  .intro {
    position: absolute;
    left: 0;
    top: 70px;
    width: 845px;
    margin: 0;
    text-align: center;
    color: var(--white);
    font-weight: 300;
    font-size: 30px;
    line-height: 35px;
  }
  .headline {
    position: absolute;
    left: 0;
    top: 248px;
    width: 862px;
    margin: 0;
    text-align: center;
    color: var(--white);
    font-weight: 500;
    font-size: 51px;
    line-height: 60px;
  }
  .headline .star { font-weight: 300; }
  .benefit {
    position: absolute;
    left: 0;
    width: 845px;
  }
  .benefit .tick {
    position: absolute;
    left: 88px;
    width: 72px;
    height: 62px;
  }
  .benefit p {
    position: absolute;
    margin: 0;
    color: var(--white);
    font-weight: 300;
    font-size: 33px;
    line-height: 40px;
    white-space: nowrap;
  }
  .benefit--price { top: 386px; }
  .benefit--price .tick { top: 10px; }
  .benefit--price p { left: 196px; top: 0; }
  .benefit--dream { top: 510px; }
  .benefit--dream .tick { top: 31px; }
  .benefit--dream p { left: 193px; top: 0; }
  .terms {
    position: absolute;
    left: 142px;
    top: 786px;
    color: var(--ink);
    font-weight: 300;
    font-size: 25px;
    line-height: 36.3px;
  }
  .terms p { margin: 0; }
  .terms ul {
    margin: 0;
    padding: 0;
    list-style: none;
  }
  .terms li {
    position: relative;
    padding-left: 37px;
  }
  .terms li::before {
    content: "";
    position: absolute;
    left: 3px;
    top: 16px;
    width: 4px;
    height: 4px;
    border-radius: 50%;
    background: var(--ink);
  }
  .brand {
    position: absolute;
    left: 0;
    top: 1078px;
    width: 845px;
  }
  .brand .lockup {
    display: flex;
    align-items: center;
    justify-content: center;
    gap: 20px;
    height: 50px;
  }
  .brand .mark {
    width: 32px;
    height: 32px;
    background: var(--leaf);
  }
  .brand .name {
    margin: 0;
    color: var(--navy);
    font-weight: 400;
    font-size: 38px;
    line-height: 50px;
    white-space: nowrap;
  }
  .brand .claim {
    margin: 6px 0 0;
    width: 845px;
    text-align: center;
    color: var(--leaf);
    font-weight: 500;
    font-size: 22px;
    letter-spacing: 1.2px;
    line-height: 28px;
  }
</style>
</head>
<body>
<main class="flyer">
  <svg class="hero-band" viewBox="0 0 845 760" aria-hidden="true">
    <defs>
      <radialGradient id="headlineGlow" cx="0.5" cy="0.5" r="0.5">
        <stop offset="0" stop-color="#a7c131"/>
        <stop offset="0.6" stop-color="#aac332"/>
        <stop offset="1" stop-color="#b0cb36" stop-opacity="0"/>
      </radialGradient>
    </defs>
    <path d="M0 0 H845 V748 C700 738 560 738 420 740 C260 742 120 735 0 706 Z" fill="var(--green)"/>
    <ellipse cx="422" cy="275" rx="400" ry="110" fill="url(#headlineGlow)"/>
  </svg>

  <p class="intro">Eine kostenlose Immobilienbewertung bekommen<br>Sie von jedem Makler, wir reduzieren zusätzlich<br>unsere Vermittlungsprovision.</p>

  <h1 class="headline">Sparen Sie jetzt 2%<span class="star">*</span> Provision</h1>

  <section class="benefit benefit--price">
    <svg class="tick" viewBox="0 0 72 62" aria-hidden="true">
      <path d="M46 4 H10 A6 6 0 0 0 4 10 V52 A6 6 0 0 0 10 58 H52 A6 6 0 0 0 58 52 V42" fill="none" stroke="var(--white)" stroke-width="5.5" stroke-linecap="round"/>
      <path d="M13 28 L27 42 L66 8" fill="none" stroke="var(--white)" stroke-width="10" stroke-linecap="round" stroke-linejoin="round"/>
    </svg>
    <p>Alles wird teurer.<br>Wir reduzieren die Provision!</p>
  </section>

  <section class="benefit benefit--dream">
    <svg class="tick" viewBox="0 0 72 62" aria-hidden="true">
      <path d="M46 4 H10 A6 6 0 0 0 4 10 V52 A6 6 0 0 0 10 58 H52 A6 6 0 0 0 58 52 V42" fill="none" stroke="var(--white)" stroke-width="5.5" stroke-linecap="round"/>
      <path d="M13 28 L27 42 L66 8" fill="none" stroke="var(--white)" stroke-width="10" stroke-linecap="round" stroke-linejoin="round"/>
    </svg>
    <p>Wir helfen bei der<br>Verwirklichung Ihres Wohntraums.<br>Angebot gültig gegen Vorlage des Flyers.</p>
  </section>

  <section class="terms">
    <p>*Bei uns 2% weniger:</p>
    <ul>
      <li>übliche Maklerprovision: 5,95%</li>
      <li>3,95% bedeutet Alleinprovision oder<br>geteilte Provision 1,97%</li>
      <li>Gilt ab einem Verkaufswert von 400.000,- Euro</li>
      <li>Gültig bis 30. Dezember 2022</li>
      <li>Nur gegen Vorlage des Flyers und Alleinauftrag</li>
    </ul>
  </section>

  <footer class="brand">
    <div class="lockup">
      <span class="mark" aria-hidden="true"></span>
      <p class="name">ORVANA GmbH</p>
    </div>
    <p class="claim">Mit Weitblick für Ihre Werte</p>
  </footer>
</main>
</body>
</html>
```